Copper Lantern Fitness Flyer

We need a Flyer designed for a Revolutionary Fresh New Functional Fitness facility in Manly Sydney, Australia. We have just recently opened and now need to get the word out. Using the flyers to hand out at events also for shop counters and letterbox drops.

Our company name is Copper Lantern Fitness "Where STRENGTH Becomes Your SPARK".
We promote health and fitness to all fitness levels concentrating on functional fitness. To learn more about us and our colour scheme see attached file and also check us out on www.brightvine-social.example/copperlanternfitnessgroup

A5 Size please

Target Market(s)

The beauty of our system is it is for everyone we have girls and guys in there teens, 20's 30's 40's and 50's. Not only that we have professional athletes, military and high fitness levels all the way to people who are overweight and need to loose weight and tone up. The system caters for everyone.

Industry/Entity Type

Fitness

Requirements
Must have
• FRONT:

Free 30min Fat Blasting Experience With Your Very Own Personal Trainer !!!

New Class Starts Every 3 minutes.
30 minute Workout With A Trainer.
No Machines No Mirrors And No Attitudes.
Catering For All Fitness Levels.
Results Guaranteed Or Your Money Back.
Fun, Fresh, Clean, Revolutionary New Facility.

Back:

You Are Just Moments Away From Burning Fat Faster Than Ever Before And Getting That Body You Always Wanted !!!

Come In Today To Claim Your FREE Workout.

Ph (02) 9417 2086
Address 5/127 Greywattle Ave Fernbrook 2178
www.brightvine-social.example/copperlanternfitnessgroup
Nice to have
• FRONT:

Back:

Ph (02) 9417 2086

```html
<!DOCTYPE html>
<html lang="en">
<head>
<meta charset="utf-8">
<title>Copper Lantern Fitness Flyer</title>
<link rel="stylesheet" href="https://fonts.googleapis.com/css2?family=Roboto+Condensed:wght@400;700;800;900&display=swap">
<style>
  :root {
    --red: #e3232c;
    --blue: #28a6dd;
    --magenta: #d3217b;
    --ink: #333333;
    --paper: #ffffff;
    --photo-light: #f3eeea;
    --photo-mid: #d9c7b8;
    --photo-dark: #9a9d9f;
  }
  html, body {
    margin: 0;
    padding: 0;
    overflow: hidden;
    background: var(--paper);
  }
  .flyer {
    position: relative;
    width: 778px;
    height: 1200px;
    overflow: hidden;
    background: var(--paper);
    font-family: "Roboto Condensed", "Arial Narrow", sans-serif;
  }
  .hero-photo {
    position: absolute;
    left: 0;
    top: 0;
    width: 560px;
    height: 1200px;
  }
  .headline-block {
    position: absolute;
    right: 22px;
    text-align: right;
    text-transform: uppercase;
    margin: 0;
    line-height: 0.95;
  }
  .offer { top: 28px; width: 440px; }
  .offer .big-red { font-size: 44px; font-weight: 800; color: var(--red); display: block; }
  .offer .big-blue { font-size: 42px; font-weight: 800; color: var(--blue); display: block; }
  .offer .small-red { font-size: 18px; font-weight: 700; color: var(--red); display: block; margin-top: 6px; line-height: 1.1; }

  .classes { top: 206px; }
  .classes .line-magenta { font-size: 54px; font-weight: 700; color: var(--magenta); display: block; }
  .classes .line-red { font-size: 78px; font-weight: 900; color: var(--red); display: block; }
  .classes .line-blue { font-size: 42px; font-weight: 400; color: var(--blue); display: block; }

  .workout { top: 396px; }
  .workout .line-magenta { font-size: 56px; font-weight: 800; color: var(--magenta); display: block; }
  .workout .line-blue { font-size: 62px; font-weight: 400; color: var(--blue); display: block; }
  .workout .line-sub { font-size: 38px; font-weight: 400; color: var(--magenta); display: block; }

  .features {
    position: absolute;
    left: 362px;
    top: 574px;
    margin: 0;
    padding: 0;
    list-style: none;
    font-size: 17px;
    line-height: 1.45;
  }
  .features .no-machines { color: var(--red); font-weight: 700; font-size: 19px; }
  .features .facility { color: var(--blue); }
  .features .guarantee { color: var(--magenta); font-weight: 700; }
  .features .levels { color: var(--ink); }

  .brand {
    position: absolute;
    right: 36px;
    top: 820px;
    display: flex;
    align-items: center;
    gap: 12px;
  }
  .brand-square {
    width: 46px;
    height: 46px;
    background: var(--blue);
  }
  .brand-name {
    font-size: 30px;
    font-weight: 700;
    color: var(--ink);
    text-transform: uppercase;
    line-height: 1;
    text-align: left;
  }

  .contact {
    position: absolute;
    right: 22px;
    top: 1030px;
    text-align: right;
  }
  .contact .phone { font-size: 38px; font-weight: 700; color: var(--red); margin: 0; }
  .contact .address { font-size: 17px; color: var(--ink); margin: 4px 0 0; }
  .web-strip {
    position: absolute;
    left: 0;
    right: 0;
    bottom: 0;
    height: 56px;
    display: flex;
    align-items: center;
    justify-content: flex-end;
    padding-right: 22px;
    font-size: 18px;
    color: var(--ink);
  }
</style>
</head>
<body>
<main class="flyer">
  <svg class="hero-photo" viewBox="0 0 560 1200" role="img" aria-label="Photo of a smiling woman in white sportswear biting a green apple while holding a bathroom scale">
    <defs>
      <linearGradient id="photo-tone" x1="0" y1="0" x2="1" y2="1">
        <stop offset="0" stop-color="var(--photo-mid)"/>
        <stop offset="0.45" stop-color="var(--photo-light)"/>
        <stop offset="1" stop-color="var(--photo-dark)"/>
      </linearGradient>
    </defs>
    <path d="M0 0 H310 C350 120 370 260 350 420 C340 520 360 600 520 660 C560 760 560 960 520 1090 C420 1130 260 1140 180 1200 H0 Z" fill="url(#photo-tone)"/>
  </svg>

  <h1 class="headline-block offer">
    <span class="big-red">Free 30min</span>
    <span class="big-blue">Fat Blasting</span>
    <span class="small-red">Experience with your very<br>own personal trainer !!!</span>
  </h1>

  <h2 class="headline-block classes">
    <span class="line-magenta">New Class</span>
    <span class="line-red">Starts</span>
    <span class="line-blue">Every 3 Minutes</span>
  </h2>

  <h2 class="headline-block workout">
    <span class="line-magenta">30 Minute</span>
    <span class="line-blue">Workout</span>
    <span class="line-sub">With a Trainer</span>
  </h2>

  <ul class="features">
    <li class="no-machines">No Machines No Mirrors &amp; No Attitudes</li>
    <li class="facility">Fun, Fresh, Clean, Revolutionary New Facility</li>
    <li class="guarantee">Results Guaranteed or Your Money Back</li>
    <li class="levels">Catering For All Fitness Levels</li>
  </ul>

  <div class="brand">
    <div class="brand-square"></div>
    <div class="brand-name">Copper Lantern<br>Fitness</div>
  </div>

  <div class="contact">
    <p class="phone">Ph (02) 9417 2086</p>
    <p class="address">5/127 Greywattle Ave Fernbrook 2178</p>
  </div>

  <div class="web-strip">www.brightvine-social.example/copperlanternfitnessgroup</div>
</main>
</body>
</html>
```